Summit Builders Web Site / Business Cards

Construction Company that specializes in Water and Fire Damage, Residential ReModels, Landscaping and Building ADU (Accessory Dwelling Unit)

Growing and changing families often need additional space, and a remodeling project can often provide that. Adding a new area, or repurposing an existing one can satisfy this requirement.

Other times, homeowners want to update the look in their kitchen or bathroom with more than just a change of cabinetry or vanity doors and drawers. Whatever your needs are, Summit Builders has skilled workers who are bonded and insured, and ready to make your dreams and visions a reality.

Target Market(s)

Home Owners

Industry/Entity Type

Construction Company

Contact Information for Business Card

Center Logo with our information on the corners

Back side to be Logo Only
Contact Info
CSLB License # 4829516
info@summitbuildersca.example
www.summitbuildersca.example

Coding

Coded - Design and coding required

Number of Pages Required

5+ page

Font styles to use
Serif
Sans Serif

Requirements
Must have
• Using our Logo Colors
Home
About Us
Services
Projects / Portfolio
Contact Us
Nice to have
• Colors matching our Logo
Should not have
• Black because it doesnt match our logo

```html
<!DOCTYPE html>
<html lang="en">
<head>
<meta charset="utf-8">
<title>Summit Builders – Construction Company in California</title>
<link href="https://fonts.googleapis.com/css2?family=Open+Sans:ital,wght@0,400;0,600;0,700;1,400&family=Ubuntu:wght@400;500;700&family=Archivo+Black&family=Merriweather:wght@400;700&display=swap" rel="stylesheet">
<style>
:root{
  --orange:#ff6600;
  --ink:#2b2d33;
  --text:#3a3c42;
  --muted:#5a5c62;
  --band:#3b4350;
  --band-dark:#323945;
  --light:#ececec;
  --gray:#d9d9d9;
  --navy:#1c3461;
  --white:#ffffff;
  --serif:'Merriweather',Georgia,serif;
  --sans:'Ubuntu',Arial,sans-serif;
}
*{margin:0;padding:0;box-sizing:border-box}
html,body{width:1200px;height:5231px;overflow:hidden}
body{position:relative;font-family:'Open Sans',Arial,sans-serif;color:var(--text);background:var(--white)}
.section{position:absolute;left:0;width:1200px;overflow:hidden}
.abs{position:absolute}
.heading{font-family:var(--serif);font-weight:700;font-size:25px;line-height:34px;color:var(--ink);white-space:nowrap}
.heading em{font-style:normal;color:var(--orange)}
.btn{position:absolute;display:flex;align-items:center;justify-content:center;background:var(--orange);color:var(--white);font-family:var(--sans);font-size:15px;font-weight:500}
.lorem{font-size:13px;line-height:18px;color:var(--muted)}

/* header */
.site-header{top:0;height:122px;background:var(--white);z-index:5}
.brand{left:57px;top:28px;display:flex;align-items:center;gap:10px}
.brand-mark{width:34px;height:34px;background:var(--orange)}
.brand-name{font-family:var(--sans);font-weight:700;font-size:22px;color:var(--ink);line-height:1}
.brand-sub{font-family:var(--sans);font-weight:700;font-size:10px;letter-spacing:3px;color:var(--ink)}
.nav a{position:absolute;top:48px;font-family:var(--sans);font-weight:500;font-size:15px;color:var(--ink);text-decoration:none}
.nav a.active{color:var(--orange)}
.nav-underline{left:278px;top:116px;width:62px;height:3px;background:var(--orange)}
.phone-box{left:843px;top:0;width:168px;height:118px;background:#e6e6e6}
.phone-box .icon{position:absolute;left:22px;top:46px;width:26px;height:26px;background:var(--orange);display:flex;align-items:center;justify-content:center}
.phone-box span{position:absolute;left:60px;top:50px;font-size:13px;font-weight:600;color:var(--ink)}
.enquire{left:1021px;top:40px;width:145px;height:36px;font-size:13px;gap:8px}

/* hero */
.hero{top:122px;height:580px;background:var(--light)}
.hero-photo{position:absolute;left:0;top:0;width:1200px;height:580px;background:linear-gradient(180deg,#3a3a38 0%,#55524c 45%,#2c2b28 100%);clip-path:polygon(0 0,100% 0,100% 68%,51% 84%,0 70%)}
.hero-title{left:0;top:128px;width:1200px;text-align:center;font-family:var(--sans);font-weight:500;font-size:45px;color:var(--white)}
.hero-sub{left:0;top:205px;width:1200px;text-align:center;font-family:var(--sans);font-size:27px;color:var(--white)}
.hero-btn{left:506px;top:283px;width:188px;height:48px}
.dots{left:572px;top:440px;display:flex;gap:8px}
.dots i{display:block;width:8px;height:8px;border-radius:50%;background:#777}
.dots i:first-child{background:var(--orange)}

/* about */
.about{top:590px;height:622px;background:var(--light)}
.about-title{left:80px;top:140px;font-family:var(--serif);font-weight:700;font-size:27px;color:var(--ink)}
.about-title em{font-style:normal;color:var(--orange)}
.about-text{left:80px;top:202px;width:560px;font-size:14.5px;line-height:29px;color:var(--text)}
.about-btn{left:80px;top:494px;width:255px;height:67px}
.about-art{left:560px;top:240px;width:630px;height:310px;background:linear-gradient(180deg,#d4d4d4,#bdbdbd);clip-path:polygon(45% 0,100% 10%,100% 100%,0 100%,0 95%,30% 95%,30% 20%)}
.cert-badge{left:680px;top:130px;width:190px;height:190px;border-radius:50%;background:var(--navy);border:6px solid var(--white);box-shadow:0 0 0 3px var(--navy)}

/* services */
.services{top:1212px;height:738px;background:var(--white)}
.services-art{left:0;top:150px;width:820px;height:588px;background:linear-gradient(90deg,#eeeeee,#f8f8f8 70%,#ffffff)}
.heading-line{position:absolute;height:2px;background:var(--ink)}
.service{position:absolute;width:260px}
.service svg{display:block;margin-bottom:8px}
.service h3{font-family:var(--sans);font-weight:700;font-size:20px;line-height:26px;color:var(--ink);margin-bottom:6px}

/* success */
.success{top:1950px;height:506px;background:var(--light)}
.value{position:absolute;width:230px}
.value .head{display:flex;align-items:center;gap:18px;margin-bottom:14px}
.value .box{width:60px;height:60px;border:3px solid var(--orange);display:flex;align-items:center;justify-content:center;flex-shrink:0}
.value h4{font-family:var(--sans);font-weight:700;font-size:16px;line-height:23px;color:var(--ink)}

/* stats */
.stats{top:2456px;height:284px;background:var(--orange)}
.stat{position:absolute;top:86px;color:var(--ink)}
.stat b{display:block;font-family:'Archivo Black',Arial,sans-serif;font-size:70px;line-height:64px;font-weight:400}
.stat span{display:block;font-family:var(--sans);font-weight:700;font-size:22px;color:var(--white);margin-top:2px}

/* projects */
.projects{top:2740px;height:938px;background:var(--white)}
.tile{position:absolute}
.tile-caption{left:36px;bottom:62px;font-family:var(--sans)}
.tile-caption strong{display:block;font-weight:500;font-size:21px;color:var(--white)}
.tile-caption span{display:block;font-size:16px;color:var(--orange);margin-top:8px}

/* testimonials */
.testimonials{top:3678px;height:599px;background:var(--gray)}
.testimonials-bg{left:0;top:0;width:1200px;height:599px;background:linear-gradient(180deg,#d6d6d6,#cfcfcf 60%,#c9c9c9)}
.quote{position:absolute;top:202px;width:335px;height:226px;background:#ececec;padding:18px 24px;font-size:14px;line-height:25.5px;color:var(--muted)}
.quote.lead{font-style:italic}
.quote::after{content:"";position:absolute;bottom:-16px;left:150px;border-left:16px solid transparent;border-right:16px solid transparent;border-top:16px solid #ececec}
.client{position:absolute;top:448px;display:flex;align-items:center;gap:12px;font-family:var(--sans);font-weight:700;font-size:15px;color:var(--ink)}
.avatar{width:44px;height:44px;border-radius:50%;background:#9e9e9e;border:2px solid var(--white)}

/* contact band */
.cta{top:4277px;height:420px;background:var(--band)}
.cta-title{left:0;top:70px;width:1200px;text-align:center;font-family:var(--serif);font-weight:700;font-size:26px;color:var(--white)}
.cta-title em{font-style:normal;color:var(--orange)}
.cta-text{left:0;top:132px;width:1200px;text-align:center;font-family:var(--sans);font-size:24px;line-height:31px;color:var(--white)}
.cta-call{left:323px;top:246px;width:266px;height:56px;font-size:19px}
.cta-enquiry{left:612px;top:246px;width:266px;height:56px;font-size:19px;background:transparent;border:3px solid var(--orange);color:var(--orange);gap:12px}

/* footer */
.site-footer{top:4670px;height:561px;background:var(--light)}
.footer-brand{left:91px;top:150px;text-align:center;width:210px}
.footer-brand .mark{width:60px;height:60px;background:var(--orange);margin:0 auto 10px}
.footer-brand .name{font-family:var(--sans);font-weight:700;font-size:46px;line-height:46px;color:var(--ink);border-top:3px solid var(--ink);padding-top:10px}
.footer-brand .sub{font-family:var(--sans);font-weight:500;font-size:14px;letter-spacing:6px;color:var(--ink);margin-top:6px}
.social{left:94px;top:338px;display:flex;gap:28px}
.social i{display:block;width:28px;height:28px;border-radius:50%;background:#555a63}
.footer-col{position:absolute;top:148px;font-size:14.5px;line-height:26.5px;color:var(--text)}
.footer-col h5{font-family:var(--serif);font-weight:700;font-size:17px;color:var(--ink);margin-bottom:14px}
.footer-col b{font-weight:600}
.copyright{left:0;top:506px;width:1200px;text-align:center;font-size:14.5px;color:var(--ink)}
</style>
</head>
<body>

<header class="section site-header">
  <div class="abs brand">
    <div class="brand-mark"></div>
    <div><div class="brand-name">SUMMIT</div><div class="brand-sub">BUILDERS</div></div>
  </div>
  <nav class="nav">
    <a class="active" style="left:290px">Home</a>
    <a style="left:378px">Company</a>
    <a style="left:491px">Projects</a>
    <a style="left:597px">Services</a>
    <a style="left:702px">Contact</a>
  </nav>
  <div class="abs nav-underline"></div>
  <div class="abs phone-box">
    <div class="icon"><svg width="14" height="14" viewBox="0 0 24 24"><path d="M6.6 10.8a15 15 0 0 0 6.6 6.6l2.2-2.2c.3-.3.7-.4 1-.2 1.1.4 2.3.6 3.6.6.6 0 1 .4 1 1V20c0 .6-.4 1-1 1A17 17 0 0 1 3 4c0-.6.4-1 1-1h3.5c.6 0 1 .4 1 1 0 1.3.2 2.5.6 3.6.1.3 0 .7-.2 1z" fill="#fff"/></svg></div>
    <span>+1 661 555 0148</span>
  </div>
  <div class="btn enquire"><svg width="18" height="13" viewBox="0 0 18 13"><rect x="1" y="1" width="16" height="11" fill="none" stroke="#fff" stroke-width="1.5"/><path d="M1 1l8 6 8-6" fill="none" stroke="#fff" stroke-width="1.5"/></svg>Enquire Now</div>
</header>

<section class="section about">
  <h2 class="abs about-title">About <em>Us</em></h2>
  <p class="abs about-text"><b>Summit Builders</b> Company specializes in Water and Fire Damage, Residential ReModels, Landscaping and Building ADU (Accessory Dwelling Unit). Growing and changing families often need additional space, and a remodeling project can often provide that. Adding a new area, or repurposing an existing one can satisfy this requirement.<br>Also homeowners want to update the look in their kitchen or bathroom with more than just a change of cabinetry or vanity doors and drawers. Whatever your needs are, Summit Builders has skilled workers who are bonded and insured, and ready to make your dreams and visions a reality.</p>
  <div class="btn about-btn">Our Services</div>
  <div class="abs about-art" role="img" aria-label="Illustration of a modern multi-storey building in orange"></div>
  <div class="abs cert-badge" role="img" aria-label="Quality certification badge"></div>
</section>

<section class="section hero">
  <div class="hero-photo" role="img" aria-label="Photo of a modern glass house at dusk surrounded by trees"></div>
  <h1 class="abs hero-title">Construction Company in California</h1>
  <p class="abs hero-sub">Creative &amp; professional service that your home needs</p>
  <div class="btn hero-btn">Find Out More</div>
  <div class="abs dots"><i></i><i></i><i></i><i></i></div>
  <svg class="abs" style="left:0;top:0" width="1200" height="580"><polygon points="950,470 1200,410 1200,580" fill="#ff6600"/></svg>
</section>

<section class="section services">
  <div class="abs services-art" role="img" aria-label="Faint sketch of a contemporary villa"></div>
  <div class="heading-line" style="left:316px;top:130px;width:106px"></div>
  <h2 class="abs heading" style="left:423px;top:94px">We Offer a Wide Range of <em>Services</em></h2>

  <div class="service" style="left:87px;top:215px">
    <svg width="52" height="50" viewBox="0 0 52 50"><path d="M4 22L26 4l22 18M10 18v28h32V18M20 46V32h12v14" fill="none" stroke="#ff6600" stroke-width="2.5"/></svg>
    <h3>Home<br>Constructions</h3>
    <p class="lorem">Lorem ipsum dolor sit amet, consectetur adipiscing elit, sed do eiusmod tempor incididunt ut labore et dolore magna aliqua.</p>
  </div>
  <div class="service" style="left:483px;top:215px">
    <svg width="52" height="50" viewBox="0 0 52 50"><rect x="4" y="6" width="40" height="40" fill="none" stroke="#ff6600" stroke-width="2.5"/><path d="M14 38l22-22 4 4-22 22h-4z" fill="none" stroke="#ff6600" stroke-width="2.5"/></svg>
    <h3>Building<br>Remodeling</h3>
    <p class="lorem">Lorem ipsum dolor sit amet, consectetur adipiscing elit, sed do eiusmod tempor incididunt ut labore et dolore magna aliqua.</p>
  </div>
  <div class="service" style="left:877px;top:215px">
    <svg width="52" height="50" viewBox="0 0 52 50"><path d="M6 30h34v10H6zM10 30v-8h26v8M10 40v6M36 40v6M30 4h14v14H30z" fill="none" stroke="#ff6600" stroke-width="2.5"/></svg>
    <h3>Interior<br>Design</h3>
    <p class="lorem">Lorem ipsum dolor sit amet, consectetur adipiscing elit, sed do eiusmod tempor incididunt ut labore et dolore magna aliqua.</p>
  </div>
  <div class="service" style="left:87px;top:455px">
    <svg width="52" height="50" viewBox="0 0 52 50"><rect x="4" y="10" width="40" height="36" fill="none" stroke="#ff6600" stroke-width="2.5"/><path d="M10 40l24-24M18 40l18-18M4 10l20-8 20 8" fill="none" stroke="#ff6600" stroke-width="2.5"/></svg>
    <h3>Exterior<br>Design</h3>
    <p class="lorem">Lorem ipsum dolor sit amet, consectetur adipiscing elit, sed do eiusmod tempor incididunt ut labore et dolore magna aliqua.</p>
  </div>
  <div class="service" style="left:483px;top:455px">
    <svg width="52" height="50" viewBox="0 0 52 50"><rect x="6" y="4" width="30" height="12" fill="none" stroke="#ff6600" stroke-width="2.5"/><path d="M36 10h6v12H22v8M18 30h8v16h-8z" fill="none" stroke="#ff6600" stroke-width="2.5"/></svg>
    <h3>Renovation<br>Services</h3>
    <p class="lorem">Lorem ipsum dolor sit amet, consectetur adipiscing elit, sed do eiusmod tempor incididunt ut labore et dolore magna aliqua.</p>
  </div>
  <div class="service" style="left:877px;top:455px">
    <svg width="52" height="50" viewBox="0 0 52 50"><path d="M14 18L28 6l14 12v12H14zM24 30v-8h8v8M4 36h12l10 6h18v4H4z" fill="none" stroke="#ff6600" stroke-width="2.5"/></svg>
    <h3>Accessory<br>Dwelling Unit (ADU)</h3>
    <p class="lorem">Lorem ipsum dolor sit amet, consectetur adipiscing elit, sed do eiusmod tempor incididunt ut labore et dolore magna aliqua.</p>
  </div>
</section>

<section class="section success">
  <div class="heading-line" style="left:360px;top:118px;width:106px"></div>
  <h2 class="abs heading" style="left:467px;top:82px">We Attribute Our <em>Success to</em></h2>

  <div class="value" style="left:57px;top:232px">
    <div class="head"><div class="box"><svg width="34" height="34" viewBox="0 0 34 34"><circle cx="17" cy="13" r="9" fill="none" stroke="#ff6600" stroke-width="2.5"/><path d="M11 20l-3 12 9-4 9 4-3-12" fill="none" stroke="#ff6600" stroke-width="2.5"/></svg></div><h4>WE'VE REPUTION<br>FOR EXCELLENCE</h4></div>
    <p class="lorem">Lorem ipsum dolor sit amet, consectetur adipiscing elit, sed do eiusmod tempor incididunt ut labore et dolore magna aliqua.</p>
  </div>
  <div class="value" style="left:349px;top:232px">
    <div class="head"><div class="box"><svg width="34" height="34" viewBox="0 0 34 34"><path d="M3 14l8-6 6 4 6-4 8 6M8 18l7 7 4-4 5 5 7-7" fill="none" stroke="#ff6600" stroke-width="2.5"/></svg></div><h4>WE BUILD<br>PARTNERSHIPS</h4></div>
    <p class="lorem">Lorem ipsum dolor sit amet, consectetur adipiscing elit, sed do eiusmod tempor incididunt ut labore et dolore magna aliqua.</p>
  </div>
  <div class="value" style="left:627px;top:232px">
    <div class="head"><div class="box"><svg width="34" height="34" viewBox="0 0 34 34"><rect x="6" y="3" width="22" height="28" fill="none" stroke="#ff6600" stroke-width="2.5"/><path d="M11 11h12M11 17h12M11 23h7" stroke="#ff6600" stroke-width="2.5"/></svg></div><h4>GUIDED BY<br>COMMITMENT</h4></div>
    <p class="lorem">Lorem ipsum dolor sit amet, consectetur adipiscing elit, sed do eiusmod tempor incididunt ut labore et dolore magna aliqua.</p>
  </div>
  <div class="value" style="left:920px;top:232px">
    <div class="head"><div class="box"><svg width="34" height="34" viewBox="0 0 34 34"><path d="M10 30V16l-4-8M24 30V16l4-8M10 16h14M14 6v10M20 6v10" fill="none" stroke="#ff6600" stroke-width="2.5"/></svg></div><h4>A TEAM OF<br>PROFESSIONALS</h4></div>
    <p class="lorem">Lorem ipsum dolor sit amet, consectetur adipiscing elit, sed do eiusmod tempor incididunt ut labore et dolore magna aliqua.</p>
  </div>
</section>

<section class="section stats">
  <div class="stat" style="left:67px"><b>53</b><span>TOTAL PROJECTS</span></div>
  <div class="stat" style="left:341px"><b>371</b><span>STAFF MEMBERS</span></div>
  <div class="stat" style="left:615px"><b>15</b><span>WORKING IN STATES</span></div>
  <div class="stat" style="left:920px"><b>2600</b><span>HOURS FOR WORK</span></div>
</section>

<section class="section projects">
  <div class="tile" style="left:24px;top:26px;width:726px;height:438px;background:linear-gradient(180deg,#b9c4cc 0%,#8a8f8a 55%,#2f6f8f 100%)" role="img" aria-label="Photo of a modern concrete villa with a swimming pool"></div>
  <div class="tile" style="left:774px;top:26px;width:402px;height:200px;background:linear-gradient(180deg,#7d8bb0,#5a6a8a 60%,#3d4450)" role="img" aria-label="Photo of a two-storey suburban house at dusk"></div>
  <div class="tile" style="left:774px;top:248px;width:402px;height:216px;background:linear-gradient(180deg,#7fb2e0,#8c8578 55%,#6d7a58)" role="img" aria-label="Photo of a small backyard accessory dwelling unit"></div>
  <div class="tile" style="left:24px;top:490px;width:565px;height:424px;background:linear-gradient(180deg,#c8d2d8,#4f4a42 55%,#5a6b3e)" role="img" aria-label="Photo of a modern dark house with glass walls and greenery"></div>
  <div class="tile" style="left:613px;top:490px;width:563px;height:424px;background:linear-gradient(180deg,#4a4c50,#404346 60%,#34423a)" role="img" aria-label="Photo of a custom home patio with pool at dusk">
    <div class="abs tile-caption"><strong>New Custom Home, Santa ana , California</strong><span>Exterior Design, Renovation Services</span></div>
  </div>
</section>

<section class="section testimonials">
  <div class="abs testimonials-bg" role="img" aria-label="Faded photo of a construction site"></div>
  <div class="heading-line" style="left:316px;top:124px;width:110px"></div>
  <h2 class="abs heading" style="left:427px;top:88px">What Our Customers Say <em>About Us</em></h2>

  <div class="quote lead" style="left:65px">SummitBuilders is one of the best general contractors we've worked with. The entire team tactfully delivered a project of exceptional quality while staying on schedule and under budget. We hope to work with Summit again in the near future!</div>
  <div class="quote" style="left:432px">Lorem ipsum dolor sit amet, consectetur adipiscing elit, sed do eiusmod tempor incididunt ut labore et dolore magna aliqua. Quis ipsum suspendisse ultrices gravida. Risus commodo viverra maecenas accumsan lacus vel facilisis.</div>
  <div class="quote" style="left:800px">Lorem ipsum dolor sit amet, consectetur adipiscing elit, sed do eiusmod tempor incididunt ut labore et dolore magna aliqua. Quis ipsum suspendisse ultrices gravida. Risus commodo viverra maecenas accumsan lacus vel facilisis.</div>

  <div class="client" style="left:240px"><div class="avatar"></div>Laura Bennett</div>
  <div class="client" style="left:610px"><div class="avatar"></div>Evan Brooks</div>
  <div class="client" style="left:978px"><div class="avatar"></div>Nora T.</div>
</section>

<section class="section cta">
  <h2 class="abs cta-title">GET IN TOUCH <em>WITH US</em></h2>
  <p class="abs cta-text">Whether you're ready to build or remodeling your home, already<br>building or just have a few questions, we're here to help.</p>
  <div class="btn cta-call">Call Us at 661-555-0148</div>
  <div class="btn cta-enquiry"><svg width="32" height="22" viewBox="0 0 32 22"><rect x="1.5" y="1.5" width="29" height="19" fill="none" stroke="#ff6600" stroke-width="2"/><path d="M1.5 1.5L16 12 30.5 1.5" fill="none" stroke="#ff6600" stroke-width="2"/></svg>Submit an Enquiry</div>
</section>

<footer class="section site-footer">
  <svg class="abs" style="left:0;top:0" width="1200" height="110">
    <polygon points="0,0 1200,0 1200,0 0,110" fill="#3b4350"/>
    <polygon points="950,70 1200,0 1200,100" fill="#ff6600"/>
  </svg>
  <div class="abs footer-brand">
    <div class="mark"></div>
    <div class="name">SUMMIT</div>
    <div class="sub">BUILDERS</div>
  </div>
  <div class="abs social"><i></i><i></i><i></i><i></i></div>

  <div class="footer-col" style="left:463px;width:330px">
    <h5>Working Hours</h5>
    <p>we work 7 days a week, every day excluding major holidays. contact us if you have an emergency, with our hotline and contact form.</p>
    <p><b>monday – friday:</b>10:00 – 16:00<br><b>saturday:</b>12:00 – 15:00<br><b>sunday and holidays:</b>09:00 – 12:00</p>
  </div>
  <div class="footer-col" style="left:869px;width:310px">
    <h5>Contact us</h5>
    <p><b>Daniel R Moreno</b> | Branch Manager<br><b>Office :</b> 661-555-0148<br><b>Direct :</b> 818-555-0173<br><b>Fax :</b> 661-555-0192<br><b style="font-size:13.5px">dmoreno@summitbuildersca.example</b><br>412 W Harbor Ave Santa Ana<br>CA 92701</p>
  </div>

  <p class="abs copyright">Copyright © 2020 Summit Builders</p>
</footer>

</body>
</html>
```